Launch of a new Investment fund

Im looking for someone design a logo and website for my Investment fund located in Singapore.

Attached to this project you will find a project scope document that details exactly what i am looking for and also includes a website copy that i have written up. I am happy for you to take your own inspiration as well to design the website. At this stage the website wont be very detailed as there isn't much information to showcase. I will require the website to be easily editable in the future so i can update it with progress the fund makes.

If you require any further details on the project please reach out to me

Coding

Coded - Design and coding required

Number of Pages Required

4 page

```html
<!DOCTYPE html>
<html lang="en">
<head>
<meta charset="utf-8">
<title>Avenor Capital Management</title>
<link href="https://fonts.googleapis.com/css2?family=Barlow+Semi+Condensed:wght@500;600;700&family=Roboto:wght@400;500;700&display=swap" rel="stylesheet">
<style>
:root{
  --navy:#11387a;
  --blue:#1d5f9f;
  --blue-light:#2f7cc0;
  --footer:#13346c;
  --text:#555b66;
  --dark:#1d1f24;
  --grey-bg:#f4f4f4;
  --line:#d6d9de;
}
*{box-sizing:border-box;margin:0;padding:0}
html,body{width:1200px;height:3349px;overflow:hidden}
body{position:relative;font-family:"Roboto",sans-serif;color:var(--text);background:#fff}
.abs{position:absolute}
.heading{font-family:"Barlow Semi Condensed",sans-serif;font-weight:600;color:var(--navy);letter-spacing:1px;text-transform:uppercase}
.btn{display:flex;align-items:center;justify-content:center;gap:8px;background:linear-gradient(90deg,var(--navy),var(--blue));color:#fff;font-weight:700;font-size:15px;text-transform:uppercase;border-radius:3px}
.btn svg{width:15px;height:15px}
p{font-size:13.5px;line-height:21.5px;text-align:justify}

/* header */
.site-header{top:0;left:0;width:1200px;height:80px;background:#fff}
.brand{left:146px;top:20px;font-family:"Barlow Semi Condensed",sans-serif;font-weight:600;color:var(--navy);font-size:30px;line-height:40px;display:flex;align-items:center;gap:10px}
.brand .mark{width:14px;height:14px;background:var(--navy)}
.main-nav{left:412px;top:28px;display:flex;gap:0;font-size:14px;font-weight:500;color:var(--dark)}
.main-nav span{margin-right:28px}
.main-nav span:nth-child(3){margin-right:15px}
.main-nav span:nth-child(4){margin-right:22px}
.login{left:920px;top:21px;width:135px;height:39px;border:1.5px solid var(--blue);border-radius:4px;color:var(--blue);font-size:14px;font-weight:500;display:flex;align-items:center;justify-content:center;gap:7px}

/* hero */
.hero{top:80px;left:0;width:1200px;height:611px;background:linear-gradient(180deg,#2b2d31 0%,#5b5e63 45%,#3a3c40 75%,#1d1e21 100%)}
.hero-title{top:283px;left:0;width:1200px;text-align:center;color:#fff;font-size:51px;line-height:60px;letter-spacing:1.5px}
.hero .btn{position:absolute}
.hero-btn{left:512px;top:432px;width:177px;height:45px}

/* what we do */
.wwd-photo{left:144px;top:775px;width:516px;height:412px;background:linear-gradient(135deg,#8c96a3,#cdd3da 50%,#5e6772)}
.wwd-card{left:562px;top:807px;width:494px;height:347px;background:#fff;box-shadow:0 4px 28px rgba(0,0,0,.08);padding:32px 30px}
.wwd-card h2{font-size:39px;line-height:40px;margin-bottom:20px}
.wwd-card p{margin-bottom:13px}
.wwd-card .btn{width:153px;height:41px;margin-top:10px}

/* team */
.team{top:1286px;left:0;width:1200px;height:498px;background:var(--grey-bg)}
.team-band{left:866px;top:1286px;width:334px;height:498px;background:linear-gradient(90deg,#1f69ad,#143c7a)}
.team-ring{left:676px;top:1345px;width:380px;height:380px;border-radius:50%;background:#fff;border:6px solid #4f86bd}
.team-photo{left:688px;top:1357px;width:356px;height:356px;border-radius:50%;background:radial-gradient(circle at 50% 40%,#d9dee4,#8d9aa9 70%,#4a5566)}
.team-text{left:143px;top:1365px;width:458px}
.team-text h2{font-size:39px;line-height:46px}
.team-text h3{font-weight:400;color:var(--blue);font-size:20px;margin:0 0 19px 6px}
.team-text p{margin:0 0 16px 6px}
.team-text .btn{width:152px;height:41px;margin:22px 0 0 6px}

/* investments */
.inv-title{top:1845px;left:0;width:1200px;text-align:center;font-size:39px}
.inv-card{top:1919px;width:292px}
.inv-card .img{height:208px}
.inv-card h4{font-size:17.5px;color:var(--dark);font-weight:500;margin:22px 0 10px 0}
.inv-card p{font-size:12.5px;line-height:20px;padding-left:1px}
.arrow-lg{width:24px;height:36px}

/* investor */
.investor{top:2317px;left:0;width:1200px;height:261px;background:var(--grey-bg)}
.investor-title{top:2366px;left:0;width:1200px;text-align:center;font-size:39px}
.partner{top:2440px;width:156px;height:80px;background:#fff;border-radius:6px;box-shadow:0 2px 10px rgba(0,0,0,.06);display:flex;align-items:center;justify-content:center}
.partner i{display:block;width:96px;height:22px;border-radius:4px;background:#c5c9cf}
.round-arrow{top:2465px;width:30px;height:30px;border-radius:50%;background:#fff;box-shadow:0 1px 6px rgba(0,0,0,.12);display:flex;align-items:center;justify-content:center}

/* contact */
.contact-title{top:2642px;left:0;width:1200px;text-align:center;font-size:39px}
.field{border:1px solid var(--line);background:#fff;font-size:13px;color:#6d727a;padding:14px 11px}
.submit{left:524px;top:2903px;width:152px;height:42px;font-size:14px}

/* footer */
.site-footer{top:3020px;left:0;width:1200px;height:329px;background:var(--footer);color:#fff}
.f-brand{left:144px;top:3097px;font-family:"Barlow Semi Condensed",sans-serif;font-weight:600;font-size:30px;display:flex;align-items:center;gap:10px}
.f-brand .mark{width:14px;height:14px;background:#fff}
.socials{left:164px;top:3181px;display:flex;gap:10px}
.socials span{width:27px;height:27px;background:#fff;border-radius:3px}
.f-col{top:3083px}
.f-col h5{font-size:15px;font-weight:700;margin-bottom:15px}
.f-col li{list-style:none;font-size:12.5px;line-height:24px}
.c-item{display:flex;gap:12px;margin-bottom:12px}
.c-item svg{width:13px;height:13px;margin-top:2px;flex:none}
.c-item b{display:block;font-size:11px}
.c-item span{font-size:12.5px;line-height:18px}
.f-rule{left:144px;top:3280px;width:912px;height:1px;background:rgba(255,255,255,.18)}
.copyright{top:3304px;left:0;width:1200px;text-align:center;font-size:13.5px}
.to-top{left:1074px;top:3263px;width:34px;height:34px;border-radius:50%;background:var(--blue-light);display:flex;align-items:center;justify-content:center}
</style>
</head>
<body>

<header class="abs site-header">
  <div class="abs brand"><span class="mark"></span>Avenor Capital</div>
  <nav class="abs main-nav"><span>Home</span><span>What we Do</span><span>Our Team</span><span>Investment</span><span>Contact Us</span></nav>
  <div class="abs login">
    <svg width="14" height="14" viewBox="0 0 16 16" fill="none" stroke="currentColor" stroke-width="1.6"><circle cx="8" cy="5" r="3"/><path d="M2.5 15c0-3 2.5-5 5.5-5s5.5 2 5.5 5z"/></svg>
    Client Login
  </div>
</header>

<section class="abs hero" role="img" aria-label="Black and white night skyline of a waterfront city">
</section>
<h1 class="abs heading hero-title">Passion for uncovering<br>new opportunities</h1>
<div class="abs btn hero-btn">Learn More
  <svg viewBox="0 0 16 16"><circle cx="8" cy="8" r="7.5" fill="#fff"/><path d="M6.5 4.5 10 8l-3.5 3.5" fill="none" stroke="#164580" stroke-width="2"/></svg>
</div>

<div class="abs wwd-photo" role="img" aria-label="Two businessmen discussing work at laptops in an office"></div>
<section class="abs wwd-card">
  <h2 class="heading">What we do</h2>
  <p>A beacon of innovative investment where strategic diversification meets meticulous market comprehension. We navigate the complexities of Global Equities, Real Estate, Venture Capital, Private Equity, and Alternative Assets, focusing on uncovering distinctive investment opportunities for our investors.</p>
  <p>At Avenor, investment is not just a transaction; it's a carefully orchestrated process, mirroring the meticulous management of personal assets.</p>
  <div class="btn">Learn More
    <svg viewBox="0 0 16 16"><circle cx="8" cy="8" r="7.5" fill="#fff"/><path d="M6.5 4.5 10 8l-3.5 3.5" fill="none" stroke="#164580" stroke-width="2"/></svg>
  </div>
</section>

<section class="abs team"></section>
<div class="abs team-band"></div>
<div class="abs team-ring"></div>
<div class="abs team-photo" role="img" aria-label="Portrait of the fund founder in a suit, arms crossed"></div>
<div class="abs team-text">
  <h2 class="heading">Our Team</h2>
  <h3>The Architect of Avenor's Visionary Path</h3>
  <p>Meet Marcus, the driving force behind Avenor Capital Management. From co-founding Australia's second-largest renewable energy company to pioneering ventures in diverse sectors, Marcus's entrepreneurial journey is marked by a passion for market innovation and sustainable growth.</p>
  <p>With over a decade of diverse business scaling experience, Marcus established Avenor Capital, evolving from personal investment to a trust-fortified endeavour of market innovation and niche investment exploration.</p>
  <div class="btn">Meet Team
    <svg viewBox="0 0 16 16"><circle cx="8" cy="8" r="7.5" fill="#fff"/><path d="M6.5 4.5 10 8l-3.5 3.5" fill="none" stroke="#164580" stroke-width="2"/></svg>
  </div>
</div>

<h2 class="abs heading inv-title">Investments</h2>
<svg class="abs arrow-lg" style="left:61px;top:2072px" viewBox="0 0 24 36"><path d="M18 4 6 18l12 14" fill="none" stroke="#8a8f96" stroke-width="3"/></svg>
<svg class="abs arrow-lg" style="left:1115px;top:2072px" viewBox="0 0 24 36"><path d="M6 4l12 14L6 32" fill="none" stroke="#8a8f96" stroke-width="3"/></svg>
<article class="abs inv-card" style="left:144px">
  <div class="img" role="img" aria-label="Team meeting around an office table" style="background:linear-gradient(135deg,#c9ccd0,#eef0f2 50%,#7d6e62)"></div>
  <h4>Venture Capital</h4>
  <p>Strategic investments in venture capital, where we harness our industry contacts and market understanding to invest in high growth startups and businesses.</p>
</article>
<article class="abs inv-card" style="left:454px">
  <div class="img" role="img" aria-label="Colleagues reviewing charts on a desk with laptop" style="background:linear-gradient(135deg,#6f8aa6,#c7b79c 55%,#e6e3de)"></div>
  <h4>Private Equity</h4>
  <p>Access to investments in cutting edge sectors, featuring companies like Northwind Labs, Chatterly, Pixelreach, Stackwell, Orbitline, Synaptix, Cargoloop, Quantra Systems and Brightforge Games.</p>
</article>
<article class="abs inv-card" style="left:763px">
  <div class="img" role="img" aria-label="Analyst studying market charts on a desktop monitor" style="background:linear-gradient(135deg,#4e5660,#a7acb2 50%,#e3e5e8)"></div>
  <h4>Global Equity Markets</h4>
  <p>We've demonstrated exceptional skill in identifying undervalued stocks and markets with high growth potential, leveraging in-depth research and market analysis.</p>
</article>

<section class="abs investor"></section>
<h2 class="abs heading investor-title">Our Investor</h2>
<div class="abs round-arrow" style="left:80px"><svg width="10" height="10" viewBox="0 0 10 10"><path d="M7 1 2 5l5 4z" fill="#222"/></svg></div>
<div class="abs round-arrow" style="left:1090px"><svg width="10" height="10" viewBox="0 0 10 10"><path d="M3 1l5 4-5 4z" fill="#222"/></svg></div>
<div class="abs partner" style="left:151px"><i></i></div>
<div class="abs partner" style="left:336px"><i></i></div>
<div class="abs partner" style="left:521px"><i></i></div>
<div class="abs partner" style="left:707px"><i></i></div>
<div class="abs partner" style="left:892px"><i></i></div>

<h2 class="abs heading contact-title">Contact Us</h2>
<div class="abs field" style="left:144px;top:2717px;width:293px;height:43px">Name</div>
<div class="abs field" style="left:454px;top:2717px;width:292px;height:43px">Email</div>
<div class="abs field" style="left:762px;top:2717px;width:293px;height:43px">Number</div>
<div class="abs field" style="left:144px;top:2778px;width:911px;height:96px">Message</div>
<div class="abs btn submit">Submit Now
  <svg viewBox="0 0 16 16"><circle cx="8" cy="8" r="7.5" fill="#fff"/><path d="M6.5 4.5 10 8l-3.5 3.5" fill="none" stroke="#164580" stroke-width="2"/></svg>
</div>

<footer class="abs site-footer"></footer>
<div class="abs f-brand" style="color:#fff"><span class="mark"></span>Avenor Capital</div>
<div class="abs socials" aria-label="Social links"><span></span><span></span><span></span><span></span></div>
<div class="abs f-col" style="left:419px;color:#fff">
  <h5>Quick Links</h5>
  <ul><li>Home</li><li>What we Do</li><li>Our Team</li><li>Our portfolio</li><li>Contact Us</li></ul>
</div>
<div class="abs f-col" style="left:599px;color:#fff">
  <h5>About Company</h5>
  <ul><li>Support</li><li>Terms &amp; Condition</li><li>Contact Us</li><li>Privacy Policy</li><li>FAQ</li></ul>
</div>
<div class="abs f-col" style="left:798px;color:#fff">
  <h5>Contact Us</h5>
  <div class="c-item"><svg viewBox="0 0 16 16"><path d="M3 1h3l1.5 4-2 1.5a9 9 0 0 0 4 4L11 8.5l4 1.5v3a2 2 0 0 1-2 2C6.5 15 1 9.5 1 3a2 2 0 0 1 2-2z" fill="#4f8fd0"/></svg><div><b>Phone</b><span>+65 6100 2040</span></div></div>
  <div class="c-item"><svg viewBox="0 0 16 16"><rect x="1" y="3" width="14" height="10" rx="1" fill="#4f8fd0"/><path d="M1.5 3.5 8 9l6.5-5.5" fill="none" stroke="#13346c" stroke-width="1.3"/></svg><div><b>Email</b><span>hello@avenorcapital.example</span></div></div>
  <div class="c-item"><svg viewBox="0 0 16 16"><path d="M8 1a5 5 0 0 1 5 5c0 4-5 9-5 9S3 10 3 6a5 5 0 0 1 5-5z" fill="#4f8fd0"/><circle cx="8" cy="6" r="1.8" fill="#13346c"/></svg><div><b>Location</b><span>18 Harbour Lane, #07-02, Singapore 018960</span></div></div>
</div>
<div class="abs f-rule"></div>
<div class="abs to-top"><svg width="12" height="12" viewBox="0 0 12 12"><path d="M2 8l4-4 4 4" fill="none" stroke="#fff" stroke-width="2"/></svg></div>
<div class="abs copyright" style="color:#fff">2024 Copyright - &nbsp;Avenor Capital Management &nbsp;| All Rights Reserved.</div>

</body>
</html>
```